Delivery Performance Dashboard for Web Portal

We need you to design a dashboard for our web portal. We deliver sand and stone to construction jobsites. The attached screenshot is from our current web portal dashboard . It shows how much material has been delivered from an order.

Dump trucks will deliver multiple loads during the day and the dispatcher uses the dashboard to monitor if they need to add more trucks or less trucks to fulfill the order. An example would be, I need to ship 1,000 tons of sand to a jobsite and I plan to use 10 trucks during the day and that it will take 10 hours of hauling to complete the job. After 5 hours of hauling (50% the day is over), I should have delivered 500 tons of sand (50% of the order). But maybe there is a lot of traffic, and I only have delivered 300 tons. The dashboard will show that I am behind schedule and I might need to add 2 more trucks to the job.

Industry/Entity Type

Construction

Font styles to use
Sans Serif

Requirements
Must have
• We need a progress bar showing how much material has been delivered, how much material was requested to be delivered total and how much material should have been delivered at the current time. The goal is to show the user if the deliveries are ahead or behind the expected pace and why.
Nice to have
• The icons for plant, driving and jobsite show if the actual times have exceeded or beaten the planned times. Maybe you have other ideas to show the user if the trucks are sitting longer on the jobsite, at the plant to get loaded or driving to and from the jobsite.

```html
<!DOCTYPE html>
<html lang="en">
<head>
<meta charset="utf-8">
<title>Delivery Dashboard</title>
<link href="https://fonts.googleapis.com/css2?family=Poppins:wght@400;500;600&display=swap" rel="stylesheet">
<style>
:root{
  --page-bg:#d0edfc;
  --panel:#ffffff;
  --main-bg:#f7f8fc;
  --line:#e9ebf0;
  --brand:#3b6cf4;
  --ink:#111318;
  --muted:#a3a8b3;
  --faint:#d6dae2;
  --track:#eef0f5;
  --alert:#f0314b;
  --online:#2fd16b;
  --ahead:#2fbf62;
  --behind:#f0314b;
  --avatar:#5cb7e6;
}
*{box-sizing:border-box;margin:0;padding:0}
html,body{width:1200px;height:977px;overflow:hidden}
body{background:var(--page-bg);font-family:'Poppins',sans-serif;position:relative}
.dashboard{position:absolute;left:0;top:126px;width:1200px;height:725px;background:var(--panel)}
.topbar{position:absolute;left:0;top:0;width:1200px;height:71px;border-bottom:1px solid var(--line);display:flex}
.brand{width:204px;height:70px;border-right:1px solid var(--line);display:flex;align-items:center;padding-left:35px;gap:10px}
.brand-mark{width:32px;height:32px;border-radius:50%;background:var(--brand)}
.brand-name{color:var(--brand);font-size:19px;font-weight:500;letter-spacing:-.2px}
.search{width:654px;display:flex;align-items:center;padding-left:52px;gap:12px;border-right:1px solid var(--line)}
.search-text{font-size:11px;color:var(--faint)}
.tool{width:73px;border-right:1px solid var(--line);display:flex;align-items:center;justify-content:center}
.tool.settings{width:72px}
.user{display:flex;align-items:center;padding-left:22px;gap:12px}
.avatar{position:relative;width:38px;height:38px;border-radius:50%;background:var(--avatar)}
.avatar .status-dot{position:absolute;right:-2px;bottom:2px;width:9px;height:9px;border-radius:50%;background:var(--online);border:1.5px solid #fff}
.user-name{font-size:13px;font-weight:500;color:var(--ink)}
.sidebar{position:absolute;left:0;top:71px;width:204px;height:597px;border-right:1px solid var(--line)}
.menu-title{position:absolute;left:35px;top:57px;display:flex;align-items:center;gap:11px;font-size:14px;font-weight:500;color:var(--ink)}
.menu-title .ring{width:14px;height:14px;border-radius:50%;border:2px solid var(--brand)}
.nav-item{position:absolute;left:0;width:204px;height:44px;display:flex;align-items:center;padding-left:35px;gap:18px;font-size:12px;color:var(--muted)}
.nav-item svg{width:18px;height:18px}
.nav-item.active{background:var(--main-bg);color:var(--brand);font-weight:500}
.nav-item.active::after{content:"";position:absolute;right:-1px;top:0;width:4px;height:44px;background:var(--brand)}
.main{position:absolute;left:204px;top:71px;width:996px;height:597px;background:var(--main-bg)}
.orders{position:absolute;left:43px;top:43px;width:911px;background:var(--panel);border-radius:4px;overflow:hidden}
.row{display:grid;grid-template-columns:73px 133px 162px 211px 81px 199px;padding-left:25px;height:65px;align-items:center;font-size:10px;color:var(--muted);white-space:nowrap}
.row:nth-child(odd){background:var(--main-bg)}
.row.head{height:54px;font-weight:600;color:var(--ink);border-bottom:1px solid var(--line);background:var(--panel)}
.row.head .sort::after{content:"";display:inline-block;margin-left:3px;border-left:3px solid transparent;border-right:3px solid transparent;border-top:4px solid var(--ink);vertical-align:middle}
.row.head .status{padding-left:5px}
.tons{display:flex;flex-direction:column;gap:8px;padding-top:6px}
.track{height:5px;border-radius:3px;background:var(--track);position:relative}
.track .fill{position:absolute;left:0;top:0;height:5px;width:53%;border-radius:3px;background:var(--brand)}
.track .expected{position:absolute;top:-3px;width:2px;height:11px;border-radius:1px;margin-left:-1px}
.track .expected.ahead{left:45%;background:var(--ahead)}
.track .expected.behind{left:62%;background:var(--behind)}
.tons-meta{display:flex;justify-content:space-between}
.footer{position:absolute;left:0;top:668px;width:1200px;height:57px;border-top:1px solid var(--line);display:flex}
.social{width:204px;border-right:1px solid var(--line);display:flex;align-items:center;justify-content:center;gap:14px}
.social span{width:12px;height:12px;border-radius:50%;background:var(--faint)}
.copyright{padding-left:42px;display:flex;align-items:center;font-size:9px;color:var(--faint)}
</style>
</head>
<body>
<div class="dashboard">
  <header class="topbar">
    <div class="brand"><span class="brand-mark"></span><span class="brand-name">LOGO HERE</span></div>
    <div class="search">
      <svg width="17" height="17" viewBox="0 0 17 17" fill="none" stroke="#d6dae2" stroke-width="1.6"><circle cx="7" cy="7" r="5.8"/><path d="M11.3 11.3 16 16"/></svg>
      <span class="search-text">Search for member and worker</span>
    </div>
    <div class="tool notifications">
      <svg width="20" height="22" viewBox="0 0 20 22"><path d="M10 2c-3.3 0-5.6 2.6-5.6 5.9v4.6L2.5 16h15l-1.9-3.5V7.9C15.6 4.6 13.3 2 10 2z" fill="#111318"/><path d="M7.6 18a2.4 2.4 0 0 0 4.8 0z" fill="#111318"/><circle cx="15.5" cy="2.5" r="2.3" fill="#f0314b"/></svg>
    </div>
    <div class="tool settings">
      <svg width="22" height="22" viewBox="0 0 24 24"><path fill="#111318" d="M19.4 13a7.5 7.5 0 0 0 0-2l2.1-1.6-2-3.5-2.5 1a7.4 7.4 0 0 0-1.7-1L15 3h-4l-.4 2.9a7.4 7.4 0 0 0-1.7 1l-2.5-1-2 3.5L6.5 11a7.5 7.5 0 0 0 0 2l-2.1 1.6 2 3.5 2.5-1a7.4 7.4 0 0 0 1.7 1L11 21h4l.4-2.9a7.4 7.4 0 0 0 1.7-1l2.5 1 2-3.5zM13 15.5a3.5 3.5 0 1 1 0-7 3.5 3.5 0 0 1 0 7z"/></svg>
    </div>
    <div class="user">
      <div class="avatar" role="img" aria-label="User avatar illustration"><span class="status-dot"></span></div>
      <span class="user-name">Never_Stop</span>
    </div>
  </header>

  <nav class="sidebar">
    <div class="menu-title"><span class="ring"></span>Menu</div>
    <div class="nav-item active" style="top:180px">
      <svg viewBox="0 0 18 18"><path d="M9 1.5 1 8.5h2.3V16h4.2v-4.5h3V16h4.2V8.5H17z" fill="#3b6cf4"/></svg>Home page
    </div>
    <div class="nav-item" style="top:240px">
      <svg viewBox="0 0 18 18" fill="none" stroke="#b8bcc6" stroke-width="1"><rect x="1.5" y="2.5" width="15" height="10"/><path d="M6 16h6M9 12.5V16M5 10l3-3 2 2 3-3"/></svg>Team data
    </div>
    <div class="nav-item" style="top:296px">
      <svg viewBox="0 0 18 18" fill="none" stroke="#b8bcc6" stroke-width="1"><rect x="1.5" y="1.5" width="15" height="15"/><path d="M4 5h1.5M7.5 5H14M4 9h1.5M7.5 9H14M4 13h1.5M7.5 13H14"/></svg>Team project
    </div>
    <div class="nav-item" style="top:350px">
      <svg viewBox="0 0 18 18" fill="none" stroke="#b8bcc6" stroke-width="1"><rect x="1.5" y="1.5" width="15" height="15"/><path d="M9 5v8M5 9h8"/></svg>Team Collect
    </div>
  </nav>

  <main class="main">
    <section class="orders">
      <div class="row head"><span class="sort">Order</span><span class="sort">Origin</span><span class="sort">Destination</span><span class="sort">Customer</span><span class="sort status">Status</span><span>Tons</span></div>
      <div class="row"><span>17746</span><span>Kestrel Asphalt Plant</span><span>BZJV - 185 from mm 77 - 98</span><span>Halvorsen Builders - North Division</span><span>Accepted</span><div class="tons"><div class="track" title="Ahead of expected pace"><div class="fill"></div><span class="expected ahead"></span></div><div class="tons-meta"><span>722.57 / 1500</span><span>7:30am - 5:00pm</span></div></div></div>
      <div class="row"><span>17746</span><span>Kestrel Asphalt Plant</span><span>BZJV - 185 from mm 77 - 98</span><span>Halvorsen Builders - North Division</span><span>Accepted</span><div class="tons"><div class="track" title="Behind expected pace"><div class="fill"></div><span class="expected behind"></span></div><div class="tons-meta"><span>722.57 / 1500</span><span>7:30am - 5:00pm</span></div></div></div>
      <div class="row"><span>17746</span><span>Kestrel Asphalt Plant</span><span>BZJV - 185 from mm 77 - 98</span><span>Halvorsen Builders - North Division</span><span>Accepted</span><div class="tons"><div class="track" title="Ahead of expected pace"><div class="fill"></div><span class="expected ahead"></span></div><div class="tons-meta"><span>722.57 / 1500</span><span>7:30am - 5:00pm</span></div></div></div>
      <div class="row"><span>17746</span><span>Kestrel Asphalt Plant</span><span>BZJV - 185 from mm 77 - 98</span><span>Halvorsen Builders - North Division</span><span>Accepted</span><div class="tons"><div class="track" title="Behind expected pace"><div class="fill"></div><span class="expected behind"></span></div><div class="tons-meta"><span>722.57 / 1500</span><span>7:30am - 5:00pm</span></div></div></div>
      <div class="row"><span>17746</span><span>Kestrel Asphalt Plant</span><span>BZJV - 185 from mm 77 - 98</span><span>Halvorsen Builders - North Division</span><span>Accepted</span><div class="tons"><div class="track" title="Ahead of expected pace"><div class="fill"></div><span class="expected ahead"></span></div><div class="tons-meta"><span>722.57 / 1500</span><span>7:30am - 5:00pm</span></div></div></div>
      <div class="row"><span>17746</span><span>Kestrel Asphalt Plant</span><span>BZJV - 185 from mm 77 - 98</span><span>Halvorsen Builders - North Division</span><span>Accepted</span><div class="tons"><div class="track" title="Ahead of expected pace"><div class="fill"></div><span class="expected ahead"></span></div><div class="tons-meta"><span>722.57 / 1500</span><span>7:30am - 5:00pm</span></div></div></div>
      <div class="row"><span>17746</span><span>Kestrel Asphalt Plant</span><span>BZJV - 185 from mm 77 - 98</span><span>Halvorsen Builders - North Division</span><span>Accepted</span><div class="tons"><div class="track" title="Behind expected pace"><div class="fill"></div><span class="expected behind"></span></div><div class="tons-meta"><span>722.57 / 1500</span><span>7:30am - 5:00pm</span></div></div></div>
    </section>
  </main>

  <footer class="footer">
    <div class="social"><span></span><span></span><span></span><span></span></div>
    <div class="copyright">Copyright ©2020 All rights reserved.</div>
  </footer>
</div>
</body>
</html>
```